IT company website design

Require a home page and an inner page designed for a company located in Ohio. The company deals with a wide range of IT services like Software development, IT based education services such as digital textbooks and BPO

Would like to get a Home page for the website and an inner page to be designed.

Design must be modern, clean and very professional. The home page should have a carousel of our services for which content will be provided.

It should give a feel that we are a large company to our prospective customers.
Updates

Hi,
In the few designs I have got for the home page, there are mockups with unwanted content/blocks like ex. latest blog posts or similar blocks. Kindly note that, we don't want this. Please follow the information about content on the home page as mentioned in the project brief. Designers, who have already submitted designs, if you can remove the unwanted blocks, it will be really appreciated.

Thanks.

I have received over 9 designs for this project, but none of them seem to be custom designed for my needs. They are just re-use of previous designs and look very out dated. Looking for fresh, clean designs following latest design trends like the ones you see in gridmarket etc.

If you can provide me a design that meets my expectations, I can definitely UP my budget for you .

Industry/Entity Type

Education

Requirements
Must have
• > > Home page > >
Home page will have

* Top Menu: Home, About Us, Solutions, Services, Contact us (should have space to accommodate for more)

* Should have a flash carousel/slide show. Each slide should be about a service we provide. Ex. a slide for bpo will have the content "Bridging the quality and cost divide in outsourcing" It should be depicted by an illustration or photograph. If you are going to use photograph, please use ones for pixvaultimages.com

* Textual content of about 200 words which we will provide

* Links in the footer along with a copyright, legal notice etc.

* Importantly, the home page should have 2 fancy buttons for "Member Login" and "Online Tutoring"

> > Inner pages > >
Will be mainly textual content explaining each of the service so, should have space for lots of textual content, with a fancy, page title (usually the service name). All inner pages should also have a side menu or something like that from where users can have a one click access to all our services.

Our logo is blue in color. with color code "0080FB". It just a stylized D with rest of the text i.e Varnex Tek Inc. our logo is of the proportion. 1:5 i.e 60px height, 300px wide. We can proportionately increase or decrease the dimensions as necessary. Color combination of the sight should be something that will go with this.

```html
<!DOCTYPE html>
<html lang="en">
<head>
<meta charset="utf-8">
<title>Varnex Tek Inc.</title>
<link rel="stylesheet" href="https://fonts.googleapis.com/css2?family=Questrial&family=Arimo:wght@400&display=swap">
<style>
:root{
  --blue:#1f74d6;
  --blue-light:#4fa3f0;
  --blue-dark:#1459b3;
  --heading:#3a90e0;
  --text:#2a2a2a;
  --page:#ffffff;
  --backdrop:#e6e6e6;
  --silver-1:#fdfdfd;
  --silver-2:#d4d4d4;
  --silver-3:#b9b9b9;
  --white:#ffffff;
}
*{margin:0;padding:0;box-sizing:border-box}
html,body{width:1200px;height:840px;overflow:hidden;background:var(--backdrop)}
body{position:relative;font-family:"Questrial",sans-serif;color:var(--text)}
.page{position:absolute;left:64px;top:0;width:1072px;height:840px;background:var(--page)}
.abs{position:absolute}
.smallcaps{font-variant:small-caps;letter-spacing:1.2px}

/* header */
.site-header{left:64px;top:0;width:1072px;height:72px;background:linear-gradient(#4d9ff0,#1c6fd3);border-radius:0 0 3px 3px}
.header-glow{left:355px;top:0;width:345px;height:72px;background:radial-gradient(ellipse at 50% 20%,rgba(255,255,255,.35),rgba(255,255,255,0) 70%)}
.brand{left:104px;top:20px;font-family:"Arimo",sans-serif;font-size:30px;color:var(--white)}
.home-link{left:566px;top:34px}
.main-nav{left:598px;top:0;height:72px;display:flex}
.main-nav a{display:block;height:72px;padding:32px 10px 0;color:var(--white);text-decoration:none;font-size:12.5px;font-weight:bold;letter-spacing:1.3px;text-transform:uppercase;border-left:2px solid var(--white);width:104px;text-align:center}
.main-nav a.active{background:linear-gradient(#2e86e4,#1c6fd3);border-left:none;width:102px}

/* quick buttons */
.quick-btn{height:28px;display:flex;align-items:center;background:linear-gradient(var(--silver-1),var(--silver-2));border:1px solid var(--silver-3);border-radius:3px;box-shadow:0 1px 2px rgba(0,0,0,.2);font-size:11px;letter-spacing:1px;font-variant:small-caps;color:#222}
.quick-btn span{flex:1;padding-left:13px}
.quick-btn i{width:38px;height:26px;background:linear-gradient(var(--blue-light),var(--blue));display:flex;align-items:center;justify-content:center;border-radius:0 2px 2px 0}

/* flash panel */
.flash-frame{left:83px;top:123px;width:468px;height:253px;background:linear-gradient(#f4f4f4,#cfcfcf);border-radius:8px;box-shadow:0 2px 4px rgba(0,0,0,.25)}
.flash-slide{left:88px;top:129px;width:458px;height:242px;border-radius:6px;background:linear-gradient(135deg,#3d3c3a 0%,#6f6c68 45%,#b4b2ad 75%,#e3e2df 100%)}
.tab{display:flex;align-items:center;background:linear-gradient(var(--silver-1),var(--silver-2));border:1px solid var(--silver-3);border-radius:3px;box-shadow:0 2px 4px rgba(0,0,0,.3);font-size:14px;letter-spacing:2px;text-transform:uppercase}
.tab span{flex:1;text-align:center}
.tab i{background:linear-gradient(var(--blue-light),var(--blue));display:flex;align-items:center;justify-content:center;height:100%;border-radius:0 2px 2px 0}

/* intro */
.intro{left:614px;top:140px;width:500px}
.heading{color:var(--heading);font-size:16.5px;letter-spacing:1.6px;font-variant:small-caps;line-height:23px}
.copy{font-size:11.4px;line-height:14.7px;letter-spacing:1.3px;font-variant:small-caps}
.intro .copy{margin-top:12px}
.intro .copy+.copy{margin-top:14.7px}

/* solutions panel */
.solutions-panel{left:83px;top:424px;width:1032px;height:416px;background:linear-gradient(#f8f8f8,#d2d2d2 20%,#e2e2e2);border-radius:6px 6px 0 0;box-shadow:0 0 3px rgba(0,0,0,.25)}
.screw{width:13px;height:13px;border-radius:50%;background:radial-gradient(circle at 40% 35%,#fff,#8a8a8a 70%);border:1px solid #7a7a7a}
.solutions-card{left:94px;top:485px;width:1011px;height:325px;background:var(--white);border-radius:10px 10px 0 0}
.solutions-left{left:125px;top:500px;width:385px}
.solutions-left .copy{margin-top:12px}
.solutions-left .copy+.copy{margin-top:14.7px}
.solutions-right-heading{left:552px;top:500px}
.thumb{width:253px;height:120px;background:linear-gradient(135deg,#e8e9ea,#9ea2a6 55%,#45484c)}
.thumb.alt{background:linear-gradient(160deg,#efe9e0 0%,#c9c2b6 40%,#6e6f71 70%,#2d2f33 100%)}
.caption{width:271px;height:47px;background:linear-gradient(#f2f2f2,#d3d3d3);border-radius:3px;padding:7px 12px 0;color:var(--heading)}
.caption b{display:block;font-weight:normal;font-size:13px;letter-spacing:1.5px;font-variant:small-caps;line-height:14px}
.caption small{display:block;font-size:9.5px;letter-spacing:1.2px;font-variant:small-caps;line-height:11px}
.solutions-bottom{left:552px;top:732px;width:545px}

/* footer */
.site-footer{left:85px;top:805px;width:1030px;height:35px;background:linear-gradient(#4d9ff0,#1c6fd3);color:var(--white);font-size:11px;letter-spacing:1.3px;font-variant:small-caps}
.copyright{left:40px;top:10px}
.footer-links{right:18px;top:10px;word-spacing:4px}
</style>
</head>
<body>
<div class="page"></div>

<header class="abs site-header"></header>
<div class="abs header-glow"></div>
<div class="abs brand">Varnex Tek Inc.</div>
<svg class="abs home-link" width="24" height="22" viewBox="0 0 24 22" aria-label="Home"><path d="M12 1 1 11h3v10h6v-6h4v6h6V11h3z" fill="#fff"/></svg>
<nav class="abs main-nav">
  <a class="active" href="#">Contact Us</a>
  <a href="#">About Us</a>
  <a href="#">Solutions</a>
  <a href="#">Services</a>
  <a href="#">Contact Us</a>
</nav>

<a class="abs quick-btn" style="left:802px;top:79px;width:150px"><span>Member Login</span><i><svg width="20" height="14" viewBox="0 0 20 14"><path d="M1 5h11V1l7 6-7 6V9H1z" fill="#fff"/></svg></i></a>
<a class="abs quick-btn" style="left:956px;top:79px;width:151px"><span>Online Tutorial</span><i><svg width="20" height="14" viewBox="0 0 20 14"><path d="M1 5h11V1l7 6-7 6V9H1z" fill="#fff"/></svg></i></a>

<section>
  <div class="abs flash-frame"></div>
  <div class="abs flash-slide" role="img" aria-label="Service slide photo: laptop on a desk with light trails and a mug"></div>
  <div class="abs tab" style="left:104px;top:118px;width:180px;height:33px"><span>Flash</span><i style="width:38px"><svg width="16" height="18" viewBox="0 0 16 18"><path d="M5 1h6v8h4l-7 8-7-8h4z" fill="#fff"/></svg></i></div>
</section>

<section class="abs intro">
  <h1 class="heading" style="font-weight:normal">Cras neque justo rhoncus a facilisis eget, nisl.</h1>
  <p class="copy">Cras neque justo, ultrices at, rhoncus a facilisis eget,nisl. Quisque vitae pede. Nam et augue. Sed a elit. Ut vel massa. Suspendisse nibh pede, ultrices vitae,ultrices nec, mollis non nibh. In sit amet pede quis leo vulputate hendrerit. Cras laoreet leo et justo auctor condimentum. Integer id enim. Suspendisse nibh pede, ultrices vitae, ultrices nec, mollis non, nibh. In sit amet pede quis leo vulputate hendrerit.</p>
  <p class="copy">Cras neque justo, ultrices at, rhoncus a facilisis eget,nisl. Quisque vitae pede. Nam et augue. Sed a elit. Ut vel massa. Suspendisse nibh pede, ultrices vitae,ultrices nec, mollis non nibh. In sit amet pede quis leo vulputate hendrerit. Cras laoreet leo et justo auctor condimentum. Integer id enim.</p>
</section>

<section>
  <div class="abs solutions-panel"></div>
  <div class="abs screw" style="left:98px;top:439px"></div>
  <div class="abs screw" style="left:1088px;top:439px"></div>
  <div class="abs solutions-card"></div>
  <div class="abs tab" style="left:450px;top:418px;width:310px;height:42px"><span>Solutions</span><i style="width:50px"><svg width="20" height="24" viewBox="0 0 16 18"><path d="M5 1h6v8h4l-7 8-7-8h4z" fill="#fff"/></svg></i></div>

  <div class="abs solutions-left">
    <h2 class="heading" style="font-weight:normal">Cras neque justo rhoncus a facilisis eget,nisl.</h2>
    <p class="copy">Cras neque justo, ultrices at, rhoncus a facilisis eget,nisl. Quisque vitae pede. Nam et augue. Sed a elit. Ut vel massa. Suspendisse nibh pede, ultrices vitae, ultrices nec, mollis non nibh. In sit amet pede quis leo vulputate hendrerit. Craslaoreet leo et justo auctor condimentum. Integer id enim. Suspendisse nibh pede, ultrices vitae, ultrices nec, mollis non, nibh. In sit amet pede quis leo vulputate hendrerit. Suspendisse nibh pede, ultrices vitae, ultrices nec, mollis non nibh.</p>
    <p class="copy">In sit amet pede quis leo vulputate hendrerit. Cras laoreet leo et justo auctor condimentum. Integer id enim.</p>
  </div>

  <h2 class="abs heading solutions-right-heading" style="font-weight:normal">Cras neque justo rhoncus a facilisis eget,nisl.</h2>
  <div class="abs thumb" style="left:549px;top:542px" role="img" aria-label="Photo: pen, mouse and keyboard on a desk"></div>
  <div class="abs caption" style="left:540px;top:662px"><b>Cras neque justo,</b><small>ultrices at, rhoncus a facilisis eget nisl.</small></div>
  <div class="abs thumb alt" style="left:836px;top:542px" role="img" aria-label="Photo: open laptop keyboard"></div>
  <div class="abs caption" style="left:827px;top:662px"><b>Cras neque justo,</b><small>ultrices at, rhoncus a facilisis eget nisl.</small></div>
  <p class="abs copy solutions-bottom">Cras neque justo, ultrices at, rhoncus a facilisis eget,nisl. Quisque vitae pede. Nam et augue. Sed a elit. Ut vel massa. Suspendisse nibh pede, ultrices vitae, ultrices nec, mollis non nibh. In sit amet pede quis leo vulpu tate hendrerit. Craslaoreet leo et justo auctor condimentum.</p>
</section>

<footer class="abs site-footer">
  <div class="abs copyright">© Copyright 2011. Varnex Tek Inc. All rights reserved.</div>
  <div class="abs footer-links">Privacy policy &nbsp;I&nbsp; Site map</div>
</footer>
</body>
</html>
```